Website Design for a "Talent Recruitment Agency"

We are looking for a website design for the website of our "Talent Recruitment Agency"; which is called "Crestline Circle".
Our recruitment website "Crestline Circle" will be focusing on: "Crestline Circle: Bridging People & Employers in Switzerland"; which means our target audience is two-folded:
(i) TALENT - that is currently residing in- or outside of Switzerland, and is open for and interested in the "Swiss Job Market".
(ii) COMPANIES - that are looking for talent for specific job vacancies in Switzerland.
With our "Crestline Circle" approach we inted to focus on Membership & Partnership:
(a)"Membership"(TALENT)
and
(b)"Partnership"(COMPANIES)
Some of the competitor sites we like are:
• www.brimlo42.dk
• www.qazet.ch
• www.plovik.ch/en
A sitemap example of our website is attached.
Also attached is a "Crestline Circle" logo in .eps format and one in .jpeg format.
We very much look forward to receive your creative ideas.
Best regards,
Crestline Circle
Crestline Circle: Bridging People & Employers in Switzerland.
Website: crestlinecircle.ch - Chirpline: CrestlineCircleCH
Target Market(s)
(i) TALENT (with around 0-10 years of working experience), currently residing in- or outside of Switzerland, but eligible to work in Switzerland.
(ii) COMPANIES (national or international) that are based in Switzerland.
Industry/Entity Type
Recruitment

```html
<!DOCTYPE html>
<html lang="en">
<head>
<meta charset="utf-8">
<title>Crestline Circle — Bridging People &amp; Employers in Switzerland</title>
<link href="https://fonts.googleapis.com/css2?family=Nunito+Sans:wght@300;400;600;700;800&family=Roboto+Condensed:wght@400;700&display=swap" rel="stylesheet">
<style>
:root{
  --orange:#f2520f;
  --orange-dark:#c9400a;
  --blue:#2f8fd3;
  --blue-deep:#1f64a8;
  --blue-light:#4aa3dc;
  --topbar:#dde9f3;
  --ink:#444;
  --muted:#777;
  --soft:#f2f2f2;
  --footer:#ececec;
  --bottom:#3b3b3b;
  --link:#2a8fd0;
}
*{box-sizing:border-box;margin:0;padding:0}
html,body{width:1024px;height:1200px;overflow:hidden}
body{position:relative;font-family:"Nunito Sans",sans-serif;color:var(--ink);background:#fff}
.abs{position:absolute}
a{color:inherit;text-decoration:none}

/* top bar */
.topbar{left:0;top:0;width:1024px;height:24px;background:var(--topbar)}
.lang{top:0;left:669px;height:24px;width:29px;background:#fff}
.flag{top:6px;width:19px;height:12px;display:flex}
.flag span{flex:1}
.account{top:6px;font-size:9px;color:#666}

/* header */
.header{left:0;top:24px;width:1024px;height:80px;background:#fff}
.brand{display:flex;align-items:center;gap:10px}
.brand-dot{width:52px;height:52px;border-radius:50%;background:var(--blue)}
.brand-name{font-weight:700;color:var(--orange);white-space:nowrap}
.nav{right:136px;top:58px;display:flex;font-size:12px;color:#555}
.nav a{padding:0 10px;border-left:1px solid #ccc;line-height:11px}
.nav a:first-child{border-left:0;color:var(--orange);font-weight:700}
.nav a:last-child{padding-right:0}
.nav-underline{left:502px;top:101px;width:36px;height:3px;background:var(--orange)}

/* hero */
.hero-photo{left:0;top:104px;width:1024px;height:401px;background:linear-gradient(100deg,#7f97b4 0%,#a9bed6 35%,#c7d6e6 60%,#aac1d9 100%)}
.hero-panel{left:520px;top:205px;width:504px;height:193px;background:var(--blue);opacity:.96;color:#fff;padding:26px 0 0 58px}
.hero-panel h1{font-size:36px;line-height:37px;font-weight:800;letter-spacing:-.5px}
.hero-panel p{margin-top:18px;font-size:19px;line-height:23px;font-weight:300;padding-left:2px}
.arrow{top:266px;width:48px;height:48px;background:rgba(60,70,85,.6);display:flex;align-items:center;justify-content:center}
.dots{left:140px;top:481px;display:flex;gap:8px;align-items:center}
.dots span{width:8px;height:8px;border-radius:50%;background:#b7c5d3}
.dots span.on{width:11px;height:11px;background:var(--blue);border:2px solid #fff}

/* audience band */
.band{left:0;top:505px;width:1024px;height:285px;background:linear-gradient(180deg,var(--blue-deep) 0%,#2a7cc4 50%,var(--blue-light) 100%)}
.card{top:544px;width:368px;height:210px;border-radius:3px;border-bottom:3px solid #dbe6ef;overflow:hidden}
.card-photo{position:absolute;inset:0}
.card-text{position:absolute;font-size:19px;line-height:28px;font-weight:300;color:#333}
.btn{position:absolute;width:136px;height:42px;background:var(--orange);border-bottom:3px solid var(--orange-dark);border-radius:3px;color:#fff;font-weight:700;font-size:14px;display:flex;align-items:center;justify-content:center}

/* latest */
.latest{left:0;top:790px;width:1024px;height:202px;background:var(--soft)}
.section-title{top:816px;display:flex;align-items:center;gap:20px;font-weight:700;font-size:14px;letter-spacing:.5px;color:#444}
.rule{height:8px;background:repeating-linear-gradient(135deg,#d8d8d8 0 1px,transparent 1px 3px)}
.job{left:138px;top:849px;width:496px;height:116px;background:#fff;box-shadow:0 1px 2px rgba(0,0,0,.08)}
.job-photo{position:absolute;left:20px;top:20px;width:76px;height:76px;background:linear-gradient(160deg,#9fb4cc,#4b5f7a);border:3px solid #fff;box-shadow:0 0 0 1px #e3e3e3}
.job-icon{position:absolute;top:64px;width:17px;height:17px;background:var(--link);display:flex;align-items:center;justify-content:center}
.job-title{position:absolute;left:112px;top:27px;font-family:"Roboto Condensed",sans-serif;font-weight:700;font-size:13px;color:#333}
.job-place{position:absolute;left:112px;top:43px;font-family:"Roboto Condensed",sans-serif;font-size:11px;color:#777}
.job-dots{position:absolute;left:357px;top:33px;display:flex;gap:5px}
.job-dots span{width:8px;height:8px;border-radius:50%;background:#e3e3e3}
.job-dots span.on{background:var(--link)}
.job-desc{position:absolute;left:112px;top:71px;width:370px;font-size:10.5px;line-height:15.5px;color:#666}
.job-desc a{color:var(--link)}
.event{left:646px;display:flex;gap:11px}
.event-thumb{width:44px;height:44px;flex:none}
.event-text{font-size:10px;line-height:16px;color:#3b5b86;margin-top:-3px}
.event-date{font-size:8.5px;font-style:italic;color:#777}

/* footer */
.footer{left:0;top:992px;width:1024px;height:170px;background:var(--footer);border-top:1px solid #e0e0e0}
.footer-about{left:136px;top:1068px;width:220px;font-size:10.5px;line-height:16px;color:#555}
.col-title{top:1018px;font-family:"Roboto Condensed",sans-serif;font-size:13px;color:#444}
.col-list{top:1043px;list-style:none;font-size:11px;line-height:24px;color:#666}
.col-list li::before{content:"›";color:var(--link);margin-right:8px}
.bottom{left:0;top:1162px;width:1024px;height:38px;background:var(--bottom);color:#8a8a8a;font-size:10.5px;padding:13px 0 0 136px}
.bottom b{color:#ddd;font-weight:400}
</style>
</head>
<body>

<div class="abs topbar"></div>
<div class="abs lang"></div>
<div class="abs flag" style="left:674px;background:#2a4a9b"></div>
<div class="abs flag" style="left:701px"><span style="background:#3a9a45"></span><span style="background:#fff"></span><span style="background:#d63a32"></span></div>
<div class="abs flag" style="left:729px;flex-direction:column"><span style="background:#222"></span><span style="background:#d22"></span><span style="background:#f2c200"></span></div>
<div class="abs flag" style="left:757px"><span style="background:#2b4ea8"></span><span style="background:#fff"></span><span style="background:#e03a3a"></span></div>
<a class="abs account" style="left:809px">Login</a>
<a class="abs account" style="left:857px">Register</a>

<header class="abs header"></header>
<div class="abs brand" style="left:133px;top:36px">
  <span class="brand-dot"></span>
  <span class="brand-name" style="font-size:29px">Crestline Circle</span>
</div>
<nav class="abs nav">
  <a>Home</a><a>About</a><a>Talent</a><a>Companies</a><a>Jobs</a><a>Events</a><a>Contact</a>
</nav>
<div class="abs nav-underline"></div>

<div class="abs hero-photo" role="img" aria-label="Businessman in a suit standing before a glass office building"></div>
<div class="abs hero-panel">
  <h1>We always bring<br>excellence.</h1>
  <p>Connecting Talent and<br>Companies in Switzerland.</p>
</div>
<div class="abs arrow" style="left:0"><svg width="12" height="16" viewBox="0 0 12 16"><path d="M9 2 3 8l6 6" stroke="#fff" stroke-width="2" fill="none"/></svg></div>
<div class="abs arrow" style="left:977px"><svg width="12" height="16" viewBox="0 0 12 16"><path d="m3 2 6 6-6 6" stroke="#fff" stroke-width="2" fill="none"/></svg></div>
<div class="abs dots"><span></span><span class="on"></span><span></span><span></span></div>

<section class="abs band"></section>
<div class="abs card" style="left:136px">
  <div class="card-photo" role="img" aria-label="Smiling businesswoman in an office" style="background:linear-gradient(90deg,#5a4a44 0%,#c9b8ad 25%,#eef1f4 45%,#f6f8fa 100%)"></div>
  <div class="card-text" style="right:32px;top:36px;text-align:right">Interested in the<br>Swiss Job Market?</div>
  <a class="btn" style="left:200px;top:134px">Register Now</a>
</div>
<div class="abs card" style="left:520px">
  <div class="card-photo" role="img" aria-label="Businessman working on a laptop" style="background:linear-gradient(90deg,#f4f3ee 0%,#eef0ef 55%,#b6b3ad 72%,#2c3444 85%,#d8dde2 100%)"></div>
  <div class="card-text" style="left:32px;top:34px">Looking for talent for<br>specific job vacancies<br>in Switzerland?</div>
  <a class="btn" style="left:32px;top:134px">Post a Job</a>
</div>

<section class="abs latest"></section>
<div class="abs section-title" style="left:138px"><span class="rule" style="width:183px"></span>LATEST JOBS<span class="rule" style="width:180px"></span></div>
<div class="abs section-title" style="left:646px;top:818px;gap:10px;font-size:14.5px"><span class="rule" style="width:52px"></span>RECENT EVENTS<span class="rule" style="width:52px"></span></div>

<article class="abs job">
  <div class="job-photo" role="img" aria-label="Candidate portrait in front of an office building"></div>
  <span class="job-icon" style="left:38px"><svg width="9" height="9" viewBox="0 0 9 9"><circle cx="3.5" cy="3.5" r="2.5" stroke="#fff" fill="none"/><path d="M5.5 5.5 8 8" stroke="#fff"/></svg></span>
  <span class="job-icon" style="left:59px"><svg width="9" height="9" viewBox="0 0 9 9"><path d="M2 7 7 2M4 2h3v3" stroke="#fff" fill="none"/></svg></span>
  <div class="job-title">Front-End Developer at&nbsp; Bluefern Labs</div>
  <div class="job-place">Sydney, Australia</div>
  <div class="job-dots"><span class="on"></span><span></span><span></span><span></span><span></span><span></span><span></span><span></span><span></span><span></span></div>
  <p class="job-desc">Lorem ipsum dolor sit amet, consectetur adipisicing elit. Proin nibh augue, suscipit a, scelerisque sed, lacinia in, mi. <a>Read More</a></p>
</article>

<div class="abs event" style="top:851px">
  <div class="event-thumb" role="img" aria-label="Business people talking" style="background:linear-gradient(135deg,#6b7684,#2f3a48)"></div>
  <div><p class="event-text">Fusce gravida tortor felis, ac dictum risus<br>lorem ipsum dolor isment sagittis.</p><p class="event-date">October 15, 2013</p></div>
</div>
<div class="abs event" style="top:913px">
  <div class="event-thumb" role="img" aria-label="Hands holding a tablet with charts" style="background:linear-gradient(135deg,#c9d6e2,#3b4656)"></div>
  <div><p class="event-text">Fusce gravida tortor felis, ac dictum risus<br>lorem ipsum dolor isment sagittis.</p><p class="event-date">October 15, 2013</p></div>
</div>

<footer class="abs footer"></footer>
<div class="abs brand" style="left:138px;top:1016px;gap:8px">
  <span class="brand-dot" style="width:40px;height:40px"></span>
  <span class="brand-name" style="font-size:22px">Crestline Circle</span>
</div>
<p class="abs footer-about">Lorem ipsum dolor sit amet, consectetur adipisicing elit. Proin nibh augue, suscipit a, scelerisque sed, lacinia in, mi. Praesent sodales velit quis augue. Cras suscipit.</p>

<div class="abs col-title" style="left:391px">NAVIGATION</div>
<ul class="abs col-list" style="left:391px"><li>Home</li><li>Jobs</li><li>Candidates</li><li>Partners</li></ul>
<ul class="abs col-list" style="left:496px"><li>About Us</li><li>Contact Us</li><li>Terms &amp; Conditions</li><li>Privacy Policy</li></ul>
<div class="abs col-title" style="left:647px">FOLLOW US</div>
<ul class="abs col-list" style="left:647px"><li>Blog</li><li>Chirpline</li><li>Friendsheet</li><li>Linkfolio</li></ul>
<div class="abs col-title" style="left:775px">POPULAR JOBS</div>
<ul class="abs col-list" style="left:775px"><li>Web Developer</li><li>Web Designer</li><li>UX Engineer</li><li>Account Manager</li></ul>

<div class="abs bottom">© Copyright 2014 <b>Company Website</b> | All Rights Reserved | Terms &amp; Conditions</div>

</body>
</html>
```